Harvest Gate Fellowship Network needs a fresh new web design

We are an up and coming multicultural church that aims to bring people into a life changing encounter with God. We need a fresh and inviting website in order to increase our internet presence and make us easier to connect with.
Here are some of the basic requirements for the site:
• Clearly displayed address, service times, and contact info
• A staff profile page
• An area for a calendar with upcoming events and their details
• Social media buttons
• Group pages for the different ministries (youth, children’s church, men, etc…)
• An area for donations and eCommerce
• A resources page for assorted media (podcasts, sermons, videos, etc.…)
• An area for prayer requests.

Industry/Entity Type

Church

```html
<!DOCTYPE html>
<html lang="en">
<head>
<meta charset="utf-8">
<title>Request Prayer – Harvest Gate Fellowship Network</title>
<link href="https://fonts.googleapis.com/css2?family=Lato:ital,wght@0,300;0,400;0,700;1,400&display=swap" rel="stylesheet">
<style>
:root{
  --indigo:#23179e;
  --indigo-deep:#1e1493;
  --gold:#e6c30b;
  --gold-text:#d8b106;
  --ink:#333;
  --muted:#555;
  --soft:#777;
  --page:#f1f1f1;
  --line:#cfcfcf;
}
*{box-sizing:border-box;margin:0;padding:0}
html,body{width:897px;height:1200px;overflow:hidden}
body{font-family:"Lato",sans-serif;background:var(--page);position:relative;color:var(--ink)}
.abs{position:absolute}

.topbar{left:0;top:0;width:897px;height:30px;background:var(--indigo);color:#fff}
.topbar .tagline{left:75px;top:9px;font-size:10px;font-weight:700}
.topbar .schedule-label{left:550px;top:9px;font-size:10.5px}
.topbar .schedule-rule{left:689px;top:6px;width:1px;height:18px;background:#fff}
.topbar .schedule-times{left:697px;top:5px;font-size:8.5px;line-height:10px}

.header{left:0;top:30px;width:897px;height:86px;background:#fff}
.brand{left:75px;top:47px;display:flex;align-items:center;gap:10px}
.brand-dot{width:34px;height:34px;border-radius:50%;background:var(--indigo)}
.brand-name{font-size:15px;font-weight:700;color:var(--indigo);line-height:17px;width:140px}
.info{top:48px;text-align:right;font-size:10px;line-height:11px;color:var(--muted)}
.info h4{font-size:12.5px;font-weight:700;color:#555;margin-bottom:4px}
.info .more{display:block;margin-top:2px;font-size:8.5px;color:var(--gold-text)}
.info.address{text-align:left}
.vrule{top:51px;width:1px;height:47px;background:#ccc}
.social{width:20px;height:20px;border-radius:50%;background:#aaa;left:802px}

.nav{left:0;top:116px;width:897px;height:30px;background:var(--gold);border-top:1px solid #d6b307}
.nav ul{list-style:none;display:flex;justify-content:space-between;margin:0 auto;width:748px;padding-top:8px}
.nav li{font-size:11px;color:#3a3000;position:relative}

.hero{left:0;top:146px;width:897px;height:75px;background:linear-gradient(90deg,#2a1b08 0%,#5b3a0e 45%,#3a2608 75%,#1e1406 100%)}
.hero .crumb{left:75px;top:21px;font-size:9.5px;color:#fff}
.hero h1{left:75px;top:34px;font-size:19px;font-weight:700;color:#fff}

.intro{left:82px;top:262px;width:420px;text-align:center;font-size:10.5px;line-height:16px;color:#444}

.card{width:153px;background:#fafafa;border:1px solid #e4e4e4;box-shadow:0 1px 2px rgba(0,0,0,.06);text-align:center;padding:12px 14px 0}
.card p{font-style:italic;font-size:9.5px;line-height:15px;color:#555;margin-bottom:15px}
.card .sep{border-top:1px dashed #aaa;margin:8px 0 6px}
.card .name{font-size:10.5px;color:#222}
.card .date{font-size:8.5px;font-style:italic;color:#555}
.card .count{width:43px;height:43px;border:2px solid var(--gold);border-radius:50%;margin:11px auto 0;font-size:18px;font-weight:700;color:var(--gold-text);line-height:39px}
.pray-btn{width:153px;height:29px;border:2px solid #555;border-radius:2px;background:#f5f5f5;font-size:10.5px;color:#555;text-align:center;line-height:25px}

.side h2{left:590px;top:262px;font-size:18px;font-weight:300;color:var(--gold-text)}
.side .underline{left:590px;top:286px;width:232px;height:1px;background:var(--gold)}
.label{left:590px;font-size:10.5px;color:#222}
.field{left:590px;width:224px;height:29px;background:#fff;border:1px solid #e2e2e2;border-radius:2px}
.submit{left:590px;top:710px;width:224px;height:33px;background:var(--gold);color:#fff;font-size:12px;text-align:center;line-height:33px;border-radius:2px}

.footer{left:0;top:974px;width:897px;height:226px;background:var(--indigo-deep);color:#c9c6f0}
.footer h3{position:absolute;top:30px;font-size:14.5px;font-weight:300;color:#fff}
.footer .txt{position:absolute;font-size:10px;line-height:13.5px}
.footer ul{list-style:none;position:absolute;font-size:9.5px;line-height:18px}
.footer .email-box{position:absolute;left:448px;top:75px;width:170px;height:25px;background:#fff;border-radius:2px;font-size:9.5px;color:#bbb;padding:7px 10px}
.footer .sub{position:absolute;left:448px;top:108px;width:70px;height:25px;background:var(--gold);color:#fff;font-size:9.5px;text-align:center;line-height:25px;border-radius:2px}
.footer .fdot{position:absolute;top:89px;width:23px;height:23px;border-radius:50%;background:#8f8ad0}
.footer .rule{position:absolute;left:75px;top:168px;width:748px;height:1px;background:#4a40b0}
.footer .copy{position:absolute;left:0;top:182px;width:897px;text-align:center;font-size:9px}
</style>
</head>
<body>

<div class="abs topbar">
  <div class="abs tagline">A house of prayer for all nations, where the love, the presence and the power of God are real.</div>
  <div class="abs schedule-label">SUNDAY SERVICE SCHEDULE</div>
  <div class="abs schedule-rule"></div>
  <div class="abs schedule-times">09:00 A.M. | Sunday School<br>10:30 A.M. | Convergent Service</div>
</div>

<div class="abs header">
  <div class="abs brand" style="top:17px"><div class="brand-dot"></div><div class="brand-name">Harvest Gate Fellowship Network</div></div>
  <div class="abs info" style="right:469px;top:18px"><h4>Donate</h4>Lorem Ipsum is simply<br>dummy text of the printing<span class="more">Donate Now »</span></div>
  <div class="abs vrule" style="left:443px;top:21px"></div>
  <div class="abs info" style="right:259px;top:18px"><h4>Request Prayer</h4>Lorem Ipsum is simply dummy text<br>of the printing and typesetting industry.<span class="more">Request Now »</span></div>
  <div class="abs vrule" style="left:654px;top:21px"></div>
  <div class="abs info address" style="left:669px;top:18px"><h4>Address</h4>Harvest Gate Fellowship<br><span style="padding-left:22px">City, Location</span><span class="more" style="text-align:right">Contact »</span></div>
  <div class="abs vrule" style="left:787px;top:21px"></div>
  <div class="abs social" style="top:22px"></div>
  <div class="abs social" style="top:45px"></div>
</div>

<nav class="abs nav">
  <ul><li>Home</li><li>About</li><li>Staff Profile</li><li>News and Events</li><li>Worship &amp; Services</li><li>Groups</li><li>Shop</li><li>Resources</li><li>Contact</li></ul>
</nav>

<div class="abs hero" role="img" aria-label="Banner photo of a golden wheat field at dusk">
  <div class="abs crumb">Home &gt; Request Prayer</div>
  <h1 class="abs">Request Prayer</h1>
</div>

<p class="abs intro">When you pray for one of the requests below, be sure to click on the <b>I prayed for you</b> button so that we can let the requestor know how many times their request has been answered.</p>

<!-- column 1 -->
<div class="abs card" style="left:82px;top:312px;height:270px"><p>Lorem Ipsum is simply dummy text of the printing and type-setting industry.</p><p>Lorem Ipsum has been the industry's standard dummy text ever since the, when an unknown printer took a galley of type and scrambled it to make a type specimen book.</p><div class="sep"></div><div class="name">JOHN DOE</div><div class="date">1-8-2014</div><div class="count">03</div></div>
<div class="abs pray-btn" style="left:82px;top:591px">I PRAY FOR YOU</div>
<div class="abs card" style="left:82px;top:635px;height:241px"><p>Lorem Ipsum is simply dummy text of the printing and type-setting industry.</p><p>Lorem Ipsum has been the industry's standard dummy text ever since the, when an unknown printer.</p><div class="sep"></div><div class="name">JOHN DOE</div><div class="date">30-7-2014</div><div class="count">17</div></div>
<div class="abs pray-btn" style="left:82px;top:884px">I PRAY FOR YOU</div>

<!-- column 2 -->
<div class="abs card" style="left:245px;top:312px;height:210px"><p>Lorem Ipsum has been the industry's standard dummy text ever since the, when an unknown printer took a galley of type and scrambled it to make a type specimen book.</p><div class="sep"></div><div class="name">JOHN DOE</div><div class="date">31-7-2014</div><div class="count">09</div></div>
<div class="abs pray-btn" style="left:245px;top:531px">I PRAY FOR YOU</div>
<div class="abs card" style="left:245px;top:575px;height:316px"><p>Lorem Ipsum is simply dummy text of the printing and type-setting industry.</p><p>Lorem Ipsum has been the industry's standard dummy text ever since the, when an unknown printer took a galley of type and scrambled it to make a type specimen book. Lorem Ipsum is simply dummy text of the printing and type-setting industry.</p><div class="sep"></div><div class="name">JOHN DOE</div><div class="date">29-7-2014</div><div class="count">32</div></div>
<div class="abs pray-btn" style="left:245px;top:900px">I PRAY FOR YOU</div>

<!-- column 3 -->
<div class="abs card" style="left:407px;top:312px;height:240px"><p>Lorem Ipsum is simply dummy text of the printing and type-setting industry.</p><p>Lorem Ipsum has been the industry's standard dummy text ever since the, when an unknown printer.</p><div class="sep"></div><div class="name">JOHN DOE</div><div class="date">31-7-2014</div><div class="count">10</div></div>
<div class="abs pray-btn" style="left:407px;top:561px">I PRAY FOR YOU</div>
<div class="abs card" style="left:407px;top:605px;height:273px"><p>Lorem Ipsum is simply dummy text of the printing and type-setting industry.</p><p>Lorem Ipsum has been the industry's standard dummy text ever since the, when an unknown printer took a galley of type and scrambled it to make a type specimen book.</p><div class="sep"></div><div class="name">JOHN DOE</div><div class="date">29-7-2014</div><div class="count">21</div></div>
<div class="abs pray-btn" style="left:407px;top:886px">I PRAY FOR YOU</div>

<!-- form -->
<div class="side">
  <h2 class="abs">REQUEST PRAYER</h2>
  <div class="abs underline"></div>
  <div class="abs label" style="top:308px">Name</div>
  <div class="abs field" style="top:325px"></div>
  <div class="abs label" style="top:360px">Country</div>
  <div class="abs field" style="top:377px">
    <svg class="abs" style="right:9px;top:11px" width="10" height="7" viewBox="0 0 10 7"><path d="M1 1l4 4 4-4" fill="none" stroke="#bbb" stroke-width="1.5"/></svg>
  </div>
  <div class="abs label" style="top:413px">Email</div>
  <div class="abs field" style="top:430px"></div>
  <div class="abs label" style="top:465px">Subject</div>
  <div class="abs field" style="top:482px"></div>
  <div class="abs label" style="top:518px">Prayer Request</div>
  <div class="abs field" style="top:535px;height:163px"></div>
  <div class="abs submit">SUBMIT</div>
</div>

<footer class="abs footer">
  <h3 style="left:74px">CONTACT US</h3>
  <div class="txt" style="left:74px;top:57px">Harvest Gate Fellowship<br>Location, city<br>State Name, Country</div>
  <svg style="position:absolute;left:75px;top:106px" width="11" height="11" viewBox="0 0 24 24"><path d="M6.6 10.8c1.4 2.8 3.8 5.1 6.6 6.6l2.2-2.2c.3-.3.7-.4 1-.2 1.1.4 2.3.6 3.6.6.6 0 1 .4 1 1V20c0 .6-.4 1-1 1C10.6 21 3 13.4 3 4c0-.6.4-1 1-1h3.5c.6 0 1 .4 1 1 0 1.3.2 2.5.6 3.6.1.3 0 .7-.2 1z" fill="#c9c6f0"/></svg>
  <div class="txt" style="left:93px;top:106px">+1 888-555-0142</div>
  <svg style="position:absolute;left:75px;top:124px" width="12" height="9" viewBox="0 0 12 9"><rect x=".5" y=".5" width="11" height="8" fill="none" stroke="#c9c6f0"/><path d="M.5.5l5.5 4.5 5.5-4.5" fill="none" stroke="#c9c6f0"/></svg>
  <div class="txt" style="left:93px;top:121px">hello@harvestgatefellowship.org</div>

  <h3 style="left:240px">COMMUNITIES WE SERVE</h3>
  <ul style="left:241px;top:54px"><li>• Lorem Ipsum</li><li>• Dummy Links</li><li>• More dummy</li><li>• Sample Text</li><li>• More samples</li></ul>
  <ul style="left:322px;top:54px"><li>• type text dummy</li><li>• Lorem Ipsum</li></ul>

  <h3 style="left:448px">NEWSLETTER</h3>
  <div class="txt" style="left:448px;top:57px">Enter your email below to get notified</div>
  <div class="email-box">Your Email</div>
  <div class="sub">Subscribe</div>

  <h3 style="left:655px">CONNECT WITH US</h3>
  <div class="txt" style="left:655px;top:57px">Stay connected for the latest updates at<br>Harvest Gate Fellowship</div>
  <div class="fdot" style="left:656px"></div>
  <div class="fdot" style="left:687px"></div>

  <div class="rule"></div>
  <div class="copy">Copyright © 2014. All rights reserved. Harvest Gate Fellowship.</div>
</footer>

</body>
</html>
```